Online Advertising: What gets us excited?

We need a poster that helps make it obvious who we are as a software delivery team.

Background: Our company's culture thrives on "ideas". We use those ideas from every member of our team to innovate and beat out the competition. We hire the kind of people that are bursting with ideas and just need a place to put them into practice.

Design Brief: In this poster design, I imagine a cross between those standard "inspirational posters", like http://lnk.example/q7tVwp

a funny cartoon, like a Odd Porch comic http://lnk.example/m3dKbx

and an PR Vandolt morphing of shapes. http://lnk.example/h8nZua

The picture should embody this: A computer programmer wrapped in ideas as an artist painting systems onto a canvas. The canvas sits on an easel that represents our suite of web advertising products. And the artist works amongst others in the Zib Media art studio, which represents our company headquarters.

The tagline might read:
"Zib Media products are the canvas where I paint my ideas!"

I am not disclosing the name of the company, so feel free to use "Zib Media". Feel free to ask any questions you like.

For the winning design, I will likely followup with additional adjustments and variations on this theme.
Updates

Project Deadline Extended
Reason: 5 days was not enough time for all of us. I did not provide feedback quickly enough for you to hone your designs. Please do continue to develop your ideas a bit, based on my feedback.

Project Deadline Extended
Reason: Allow for more designs. None of the images are exactly hitting that right sense of creativity and software creation, being combined.

Target Market(s)

Our employees, especially our engineering team of programmers, testers, web designers, project managers, and product managers.

Industry/Entity Type

Software

Font styles to use
Sans Serif

Requirements
Must have
• Immediate appeal. Easy to understand at a glance, yet nuanced deeper meaning.
Nice to have
• Fine details that intrigue people.
Should not have
• Gender bias - must support men and women. Racial bias - must not exclude any races.

```html
<!DOCTYPE html>
<html lang="en">
<head>
<meta charset="utf-8">
<title>Zib Media products – The Canvas</title>
<link rel="stylesheet" href="https://fonts.googleapis.com/css2?family=Special+Elite&display=swap">
<style>
  :root {
    --ink: #111111;
    --teal: #7dcfcf;
    --teal-shade: rgba(25, 45, 55, 0.55);
    --paper: #ffffff;
    --plum: #5a2f5e;
    --wine: #6e2c35;
    --wood: #7a3b35;
    --violet: #8e6aa6;
    --slate: #6d7f96;
  }
  html, body {
    margin: 0;
    padding: 0;
    overflow: hidden;
    background: var(--paper);
  }
  .poster {
    position: relative;
    width: 1200px;
    height: 805px;
    overflow: hidden;
    background: var(--paper);
  }
  .scene-desk {
    position: absolute;
    left: 0;
    top: 0;
    width: 640px;
    height: 805px;
    background:
      radial-gradient(ellipse 260px 180px at 130px 90px, rgba(120, 150, 170, 0.75), transparent 70%),
      radial-gradient(ellipse 300px 200px at 320px 600px, rgba(230, 220, 235, 0.8), transparent 70%),
      radial-gradient(ellipse 220px 260px at 560px 220px, rgba(110, 40, 55, 0.85), transparent 70%),
      linear-gradient(160deg, var(--slate) 0%, var(--plum) 35%, var(--wood) 60%, var(--violet) 85%, var(--wine) 100%);
  }
  .scene-strokes {
    position: absolute;
    left: 640px;
    top: 0;
    width: 560px;
    height: 805px;
    background:
      radial-gradient(ellipse 200px 260px at 120px 220px, rgba(143, 132, 184, 0.55), transparent 70%),
      radial-gradient(ellipse 220px 200px at 380px 560px, rgba(185, 120, 175, 0.5), transparent 70%),
      radial-gradient(ellipse 160px 220px at 60px 700px, rgba(160, 150, 200, 0.45), transparent 70%),
      linear-gradient(180deg, #f3eff7 0%, #ece4f1 50%, #efe7f2 100%);
  }
  .type-layer {
    position: absolute;
    inset: 0;
    width: 1200px;
    height: 805px;
    font-family: "Special Elite", "Courier New", monospace;
  }
  .brand-line { fill: var(--ink); font-size: 58px; }
  .headline { fill: var(--teal); filter: drop-shadow(3px 4px 3px var(--teal-shade)); }
  .headline-the { font-size: 160px; }
  .headline-canvas { font-size: 300px; }
  .tagline { fill: var(--ink); font-size: 80px; }
</style>
</head>
<body>
  <main class="poster">
    <div class="scene-desk" role="img" aria-label="Photo of a desk with a monitor and a tablet showing a yearly calendar, overlaid with purple, teal and red paint strokes on a canvas texture"></div>
    <div class="scene-strokes" role="img" aria-label="Loose lavender, blue and pink watercolour brush strokes on white canvas texture"></div>

    <svg class="type-layer" viewBox="0 0 1200 805" aria-labelledby="poster-title">
      <title id="poster-title">Zib Media products – The Canvas where I paint my ideas!</title>
      <text class="brand-line" x="655" y="115" textLength="500" lengthAdjust="spacingAndGlyphs">Zib Media products</text>
      <g class="headline">
        <text class="headline-the" x="148" y="382" textLength="192" lengthAdjust="spacingAndGlyphs">The</text>
        <text class="headline-canvas" x="345" y="385" textLength="660" lengthAdjust="spacingAndGlyphs">Canvas</text>
      </g>
      <text class="tagline" x="565" y="465" textLength="485" lengthAdjust="spacingAndGlyphs">where I paint</text>
      <text class="tagline" x="640" y="537" textLength="320" lengthAdjust="spacingAndGlyphs">my ideas!</text>
    </svg>
  </main>
</body>
</html>
```